public page kestrel AX (www.kestrelax.com)

https://www.plumaquill.com/shard/s418/sh/b2190ce7-5d3a-4f1e-8c2b-6e7a1d94c0f2/47b1e9c2d0a83f56e1c7b9a2f4d60e81

compatible with wordpress

Designs look the same

Industry/Entity Type

Finance And Accounting

Coding

Coded - Design and coding required

Number of Pages Required

1 page

Font styles to use
Sans Serif

Colors
85cae6
3176b5
cfdeed
fac994
fff3d1
fefdec
cfcfcf
e8e8e8
9d9d9d

```html
<!DOCTYPE html>
<html lang="en">
<head>
<meta charset="utf-8">
<title>kestrel AX</title>
<link rel="stylesheet" href="https://fonts.googleapis.com/css2?family=Lato:wght@300;400;700&display=swap">
<style>
:root{
  --blue:#3176b5;--blue-dark:#1f5f9e;--sky:#85cae6;--ice:#cfdeed;
  --orange:#f28a1e;--peach:#fac994;--cream:#fff3d1;
  --grey-1:#e8e8e8;--grey-2:#cfcfcf;--grey-3:#9d9d9d;--ink:#333;--white:#fff;
}
*{margin:0;padding:0;box-sizing:border-box}
html,body{width:1200px;height:3267px;overflow:hidden}
body{position:relative;font-family:'Lato',sans-serif;color:var(--ink);background:var(--white)}
.abs{position:absolute}
.hero-bg{left:0;top:0;width:1200px;height:660px}
.logo{left:163px;top:30px;display:flex;align-items:center;gap:8px;color:var(--white);font-weight:700;font-size:17px;letter-spacing:.5px}
.logo i{width:14px;height:14px;border-radius:50%;background:var(--white);display:block}
.nav{top:36px;left:0;width:1200px;height:20px;color:var(--white);font-size:15px}
.nav span{position:absolute}
.btn-sm{position:absolute;top:33px;height:28px;width:70px;background:var(--orange);color:var(--white);font-size:11px;font-weight:700;display:flex;align-items:center;justify-content:center}
.dropdown{left:377px;top:72px;width:385px;height:357px;background:var(--white);box-shadow:0 4px 14px rgba(0,0,0,.15)}
.dropdown .item{position:absolute;left:56px;display:flex;align-items:center;gap:12px;font-size:16px;color:#222}
.dropdown p{position:absolute;left:56px;top:247px;width:290px;font-size:13px;line-height:22px;color:#222}
.hero-title{left:0;width:1200px;top:205px;text-align:center;color:var(--white);font-size:46px;font-weight:700;letter-spacing:1px}
.hero-sub{left:0;width:1200px;top:274px;text-align:center;color:var(--white);font-size:20px;font-weight:300}
.signup{left:331px;top:331px;width:538px;height:52px;border-radius:26px;background:var(--white);display:flex;align-items:center;overflow:hidden}
.signup span{padding-left:20px;font-size:13px;color:#555;flex:1}
.signup b{width:200px;height:52px;border-radius:26px;background:var(--orange);color:var(--white);display:flex;align-items:center;justify-content:center;font-size:15px}
.dot{top:521px;width:18px;height:18px;border-radius:50%;background:var(--white)}
.dot.active{background:transparent;border:2px solid var(--white)}
.media{background:linear-gradient(135deg,#dbe8f2,#9fb4c8)}
.card-frame{left:161px;top:754px;width:405px;height:361px;background:var(--white);box-shadow:0 3px 12px rgba(0,0,0,.25);padding:18px}
.badge{width:74px;height:74px;border-radius:50%;background:var(--peach);display:flex;align-items:center;justify-content:center}
.h2{font-size:27px;font-weight:300;line-height:31px;color:#333}
.copy{font-size:11.5px;line-height:20px;color:#333}
.link{font-size:18px;color:var(--orange);text-decoration:underline}
.avatar{left:623px;top:1037px;width:67px;height:67px;border-radius:50%;background:linear-gradient(#b8c2cc,#6b7784)}
.band{left:0;top:1650px;width:1200px;height:630px}
.price-line{left:0;width:1200px;text-align:center}
.cta{left:503px;top:2049px;width:194px;height:46px;border-radius:23px;background:var(--orange);color:var(--white);font-weight:700;font-size:15px;display:flex;align-items:center;justify-content:center;letter-spacing:.5px}
.faq{left:355px;width:490px;height:46px;border:1px solid var(--grey-2);display:flex;align-items:center;justify-content:space-between;padding:0 14px;font-size:13.5px;color:var(--blue-dark)}
.faq b{font-weight:400;font-size:18px}
.footer-bg{left:0;top:2680px;width:1200px;height:587px}
.f-col{font-size:11.5px;line-height:24px;color:#333}
.f-head{font-size:18px;color:#333;line-height:24px;margin-bottom:8px}
.f-logo{left:934px;top:2760px;display:flex;align-items:center;gap:8px;color:var(--grey-3);font-weight:700;font-size:17px}
.f-logo i{width:14px;height:14px;border-radius:50%;background:var(--grey-3);display:block}
.social{top:3156px;width:22px;height:22px;border-radius:50%;background:#333}
.rule{left:161px;top:3206px;width:1000px;height:1px;background:var(--grey-2)}
.legal{top:3232px;font-size:12px;color:#333}
</style>
</head>
<body>

<svg class="abs hero-bg" viewBox="0 0 1200 660" role="img" aria-label="Office scene photo tinted blue to orange">
  <defs><linearGradient id="hg" x1="0" y1="0" x2="1" y2="1"><stop offset="0" stop-color="#2e6fae"/><stop offset=".55" stop-color="#5d7c98"/><stop offset="1" stop-color="#f08a22"/></linearGradient></defs>
  <polygon points="0,0 1200,0 1200,500 0,656" fill="url(#hg)"/>
</svg>

<div class="abs logo"><i></i>kestrel AX</div>
<nav class="abs nav">
  <span style="left:375px">Home</span><span style="left:457px">Pricing</span>
  <span style="left:545px">About Us</span><span style="left:649px">Contact</span>
  <span style="left:743px">Blog</span><span style="left:816px">FAQ</span>
</nav>
<div class="btn-sm" style="left:882px">SIGN UP</div>
<div class="btn-sm" style="left:967px">SIGN IN</div>

<h1 class="abs hero-title">WELCOME TO KESTREL AX</h1>
<p class="abs hero-sub">Lorem ipsum dolor sit amet, consectetur r sit amet</p>
<div class="abs signup"><span>Email</span><b>GET STARTED</b></div>
<div class="abs dot" style="left:567px"></div>
<div class="abs dot active" style="left:590px"></div>
<div class="abs dot" style="left:614px"></div>

<div class="abs dropdown">
  <svg class="abs" style="left:186px;top:-8px" width="14" height="8"><polygon points="0,8 7,0 14,8" fill="#fff"/></svg>
  <div class="item" style="top:26px"><svg width="18" height="18"><circle cx="9" cy="5" r="4" fill="#555"/><path d="M2 18c0-5 3-7 7-7s7 2 7 7z" fill="#555"/></svg>Sed ut perspiciatis</div>
  <div class="item" style="top:63px"><svg width="18" height="18"><polygon points="1,9 17,2 12,16 9,11" fill="#3d8c5a"/></svg>Unde omnis iste</div>
  <div class="item" style="top:100px"><svg width="18" height="18"><rect x="2" y="10" width="3" height="7" fill="#3176b5"/><rect x="7" y="6" width="3" height="11" fill="#f28a1e"/><rect x="12" y="3" width="3" height="14" fill="#3176b5"/></svg>Natus error sit</div>
  <div class="item" style="top:135px"><svg width="18" height="18"><rect x="2" y="6" width="4" height="11" fill="#c07a2a"/><rect x="7" y="3" width="4" height="14" fill="#3176b5"/><rect x="12" y="8" width="4" height="9" fill="#c07a2a"/></svg>Voluptatem</div>
  <div class="item" style="top:172px"><svg width="18" height="18"><polygon points="9,1 11.4,6.6 17.5,7 12.8,11 14.3,17 9,13.7 3.7,17 5.2,11 .5,7 6.6,6.6" fill="#3a8a86"/></svg>Accusantium</div>
  <div class="item" style="top:217px"><svg width="18" height="18"><rect x="1" y="3" width="16" height="12" fill="none" stroke="#3176b5" stroke-width="2"/><rect x="4" y="6" width="5" height="5" fill="#f28a1e"/></svg>Voluptatem</div>
  <p>Lorem ipsum dolor sit amet, consectetur adipis cing elit, sed do eiusmodtempr incididunt ut labore et dolore</p>
</div>

<div class="abs card-frame"><div class="media" role="img" aria-label="Illustration of a phone showing a rising finance chart" style="width:100%;height:100%"></div></div>

<div class="abs badge" style="left:616px;top:753px"><svg width="40" height="40"><polyline points="4,34 14,22 22,27 36,8" fill="none" stroke="#f28a1e" stroke-width="3"/><line x1="4" y1="36" x2="38" y2="36" stroke="#f28a1e" stroke-width="2"/></svg></div>
<h2 class="abs h2" style="left:703px;top:754px;width:340px">Lorem ipsum dolor sit amet, consectetur adipis</h2>
<p class="abs copy" style="left:623px;top:839px;width:390px">Lorem ipsum dolor sit amet, consectetur adipiscing elit, sed do eiusmod tempor incididunt ut labore et dolore magna aliquat e</p>
<a class="abs link" style="left:621px;top:901px">Donsectetur adipiscin</a>
<p class="abs copy" style="left:623px;top:944px;width:390px">Lorem ipsum dolor sit amet, consectetur adipiscing elit, sed do eiusmod tempor incididunt ut labore et dolore magna aliquat enim ad minim veniam, quis nostrud exercitation ullamco laboris nisi ut aliquip ex ea commodo consequat.uis aute irure dolor in reprehende.</p>
<div class="abs avatar" role="img" aria-label="Portrait photo of the head of product design"></div>
<p class="abs copy" style="left:700px;top:1045px"><span style="color:var(--blue)">Mara</span> Head of Product Design</p>
<div class="abs" style="left:700px;top:1071px;width:26px;height:26px;border-radius:50%;border:2px solid #555"></div>

<div class="abs badge" style="left:159px;top:1228px"><svg width="40" height="40"><rect x="6" y="22" width="5" height="12" fill="#f28a1e"/><rect x="14" y="14" width="5" height="20" fill="#f28a1e"/><rect x="22" y="18" width="5" height="16" fill="#f28a1e"/><rect x="30" y="10" width="5" height="24" fill="#f28a1e"/></svg></div>
<h2 class="abs h2" style="left:248px;top:1229px;width:340px">Lorem ipsum dolor sit amet, consectetur adipis</h2>
<p class="abs copy" style="left:165px;top:1312px;width:390px">Lorem ipsum dolor sit amet, consectetur adipiscing elit, sed do eiusmod tempor incididunt ut labore et dolore magna aliquat e</p>
<a class="abs link" style="left:163px;top:1373px">Donsectetur adipiscin</a>
<p class="abs copy" style="left:165px;top:1417px;width:410px">Lorem ipsum dolor sit amet, consectetur adipiscing elit, sed do eiusd tempor incididunt ut labore et dolore magna aliquat enim ad minim veniamlore, quis nostrud exercitation ullamco laboris nisi ut aliquip ex ea commo doconsequa t.uis autrud exercitation ullamco laboris nisi ut aliquip ex ea lorecommodo consequat.uis aute irure dolor in reprehende.te irure doullamco laboris nisi ut aliquip ex ea commodo consequat.uis aute irure dolo.</p>
<div class="abs media" role="img" aria-label="Photo of colleagues reviewing financial charts beside a laptop" style="left:632px;top:1198px;width:405px;height:362px;background:linear-gradient(135deg,#c9b89c,#7c8fa6 60%,#3d4c5e);box-shadow:0 3px 12px rgba(0,0,0,.25)"></div>

<svg class="abs band" viewBox="0 0 1200 630" role="img" aria-label="Faint grey geometric network background">
  <polygon points="0,100 1200,0 1200,540 0,630" fill="#e8e8e8"/>
</svg>
<div class="abs badge" style="left:563px;top:1840px;background:var(--peach)"><svg width="44" height="44"><circle cx="22" cy="22" r="15" fill="none" stroke="#f28a1e" stroke-width="3"/></svg></div>
<p class="abs price-line" style="top:1925px;font-size:28px;font-weight:300">Complete kestrel AX solutions only</p>
<p class="abs price-line" style="top:1968px;font-size:46px;color:var(--blue)">$2.95/month*</p>
<div class="abs cta">GET STARTED NOW</div>

<div class="abs badge" style="left:563px;top:2265px"><span style="font-size:44px;font-weight:700;color:var(--orange)">?</span></div>
<h2 class="abs price-line" style="top:2347px;font-size:31px;font-weight:300">FAQs</h2>
<div class="abs faq" style="top:2409px">Donec at sapien quis tellus convallis imperdiet.<b>+</b></div>
<div class="abs faq" style="top:2461px">Integer vel massa vel turpis dapibus consectetur eu sed ligula.<b>+</b></div>
<div class="abs faq" style="top:2513px">Morbi et nisi non ex scelerisque sodales vitae ut risus.<b>+</b></div>
<div class="abs faq" style="top:2565px">Vestibulum ut quam ut massa viverra fringilla ac nec felis.<b>+</b></div>
<div class="abs faq" style="top:2617px">Vestibulum ut quam ut massa viverra fringilla ac nec felis.<b>+</b></div>

<svg class="abs footer-bg" viewBox="0 0 1200 587" role="img" aria-label="Light grey footer background with faint hexagon pattern">
  <polygon points="0,70 1200,0 1200,587 0,587" fill="#f1f1f1"/>
</svg>
<div class="abs f-logo"><i></i>kestrel AX</div>

<div class="abs f-col" style="left:161px;top:2838px;width:200px">
  <div class="f-head"><svg width="18" height="18" style="vertical-align:-3px;margin-right:8px"><path d="M9 1a6 6 0 0 1 6 6c0 5-6 10-6 10S3 12 3 7a6 6 0 0 1 6-6z" fill="none" stroke="#777" stroke-width="1.5"/><circle cx="9" cy="7" r="2" fill="#777"/></svg>Address</div>
  Kestrelax<br>14 Harrow Lane Wendmoor<br>Norfolk NR99 4QZ<br>England
  <div class="f-head" style="margin-top:18px"><svg width="20" height="14" style="vertical-align:0;margin-right:8px"><rect x="1" y="1" width="18" height="12" fill="none" stroke="#777" stroke-width="1.5"/><polyline points="1,1 10,8 19,1" fill="none" stroke="#777" stroke-width="1.5"/></svg>Email</div>
  info@kestrelax.com
  <div class="f-head" style="margin-top:18px"><svg width="16" height="16" style="vertical-align:-2px;margin-right:8px"><path d="M3 1l3 0 1 4-2 1.5a9 9 0 0 0 4.5 4.5L11 9l4 1v3c0 1-1 2-2 2A12 12 0 0 1 1 3c0-1 1-2 2-2z" fill="none" stroke="#777" stroke-width="1.4"/></svg>Phone</div>
  01632 555014
</div>

<div class="abs f-col" style="left:394px;top:2838px"><div class="f-head">About Us</div>Sed ut pers<br>Gtis unde omnis<br>Tnatus error<br>Sit voluptatem<br>Accusantium<br>Doloremque<br>Kudantium,<br>Totam rem<br>Aperiam</div>
<div class="abs f-col" style="left:573px;top:2838px"><div class="f-head">Developers</div>Sed ut pers<br>Gtis unde omnis<br>Sit voluptatem
  <div class="f-head" style="margin-top:26px">Company</div>Sed ut pers<br>Gtis unde omnis<br>Tnatus error<br>Sit voluptatem</div>
<div class="abs f-col" style="left:762px;top:2838px"><div class="f-head">Resources</div>Sed ut pers<br>Gtis unde omnis<br>Tnatus error<br>Sit voluptatem
  <div class="f-head" style="margin-top:12px">Support</div>Sed ut pers<br>Gtis unde omnis<br>Tnatus error<br>Gtis unde omnis<br>Tnatus error</div>
<div class="abs f-col" style="left:941px;top:2838px"><div class="f-head">More Links</div>Sed ut pers<br>Gtis unde omnis<br>Tnatus error<br>Sit voluptatem<br>Accusantium<br>Doloremque<br>Kudantium,<br>Totam rem<br>Aperiam</div>

<div class="abs social" style="left:161px"></div>
<div class="abs social" style="left:203px"></div>
<div class="abs social" style="left:241px"></div>
<div class="abs social" style="left:273px"></div>
<div class="abs rule"></div>
<p class="abs legal" style="left:161px">Copyright © 2018. All rights reserved. Privacy Policy &nbsp;&nbsp; Terms of Use &nbsp;&nbsp; Legal &nbsp;&nbsp; Site Map</p>
<p class="abs legal" style="left:966px;top:3228px;font-size:10px"><span style="display:inline-block;width:10px;height:8px;background:var(--grey-3);margin-right:4px"></span>United States</p>

</body>
</html>
```